Harbor Crest Vitality.com Landing Page

Create a well designed home/landing page using that communicates the feeling of Harbor Crest Vitality with this sections that scroll from top to bottom -
Top section - Displays "Harbor Crest Vitality" with space for embedded YouTube video.

The following sections follow the top section -
Assess your current Harbor Crest Vitality. Complete our free life balance assessment to identify key areas where you you will most benefit.
"Learn more" call to action button

Create a Harbor Crest Vitality Learning Portal account. Get a 14 day free trial to a wealth of learning activities, motivational videos and professional presentations on our learning portal designed specifically to address the eight essential areas of Harbor Crest Vitality.
"Register now" call to action button

Get weekly reports on your progress and goal achievement. Celebrate your success each week as you review your progress on each life balance area.

Appropriate royalty free photos and graphics that fit the chosen theme you recommend.

I'm reviewing the designs. I realize that I need to clarify that Harbor Crest Vitality focuses on eight areas, not just physical fitness and meditation. Spirituality and Sense of Purpose; Fitness and Health; Relationships; Personal Finance; Recreation and Fun; Physical Environment; Personal Development and Learning; Work and Career

1 page

33a6d7
00a990
9bcb3c
2f73b3

```html
<!DOCTYPE html>
<html lang="en">
<head>
<meta charset="utf-8">
<title>Harbor Crest Vitality</title>
<link rel="stylesheet" href="https://fonts.googleapis.com/css2?family=Raleway:wght@300;500;600;700&display=swap">
<style>
:root{
  --sky:#33a6d7;
  --teal:#00a990;
  --lime:#9bcb3c;
  --navy:#2f73b3;
  --ink:#222222;
  --body:#444444;
  --mist:#f4f4f4;
  --alert:#e01010;
  --night:#000000;
}
*{margin:0;padding:0;box-sizing:border-box}
html,body{width:1200px;height:2381px;overflow:hidden}
body{font-family:"Raleway",sans-serif;background:#fff;position:relative}
.hero{position:absolute;left:0;top:0;width:1200px;height:602px;
  background:linear-gradient(180deg,#202324 0%,#3c4a50 30%,#4f7c86 55%,#2f6c73 75%,#1f4b3a 100%)}
.hero-title{position:absolute;top:156px;width:100%;text-align:center;color:#fff;font-weight:300;font-size:41px;letter-spacing:.3px}
.play{position:absolute;left:570px;top:221px;width:60px;height:60px}
.menu{position:absolute;left:1117px;top:40px;width:34px;height:16px}
.assess{position:absolute;left:0;top:602px;width:1200px;height:602px;background:var(--mist)}
.assess h2{position:absolute;left:109px;top:102px;color:var(--teal);font-size:35px;font-weight:600;letter-spacing:.2px}
.assess p{position:absolute;left:109px;top:178px;width:720px;color:var(--teal);font-size:19.5px;font-weight:600;line-height:30px}
.btn{position:absolute;display:flex;align-items:center;justify-content:center;width:218px;height:66px;color:#fff;font-size:20px;font-weight:600}
.btn-teal{left:109px;top:278px;background:var(--teal)}
.assess-photo{position:absolute;left:612px;top:326px;width:588px;height:276px;background:linear-gradient(160deg,#4e7d3c,#2f5a27 60%,#5a7f4e)}
.wedge{position:absolute;left:612px;top:1204px}
.portal{position:absolute;left:0;top:1204px;width:1200px}
.portal h2{position:absolute;left:58px;top:102px;width:1120px;color:var(--ink);font-size:35px;font-weight:600;white-space:nowrap}
.portal p{position:absolute;left:58px;top:166px;width:1040px;color:var(--body);font-size:19.5px;font-weight:500;line-height:30px}
.portal .trial{color:var(--alert)}
.btn-sky{left:58px;top:294px;background:var(--sky);box-shadow:0 3px 6px rgba(0,0,0,.2)}
.reports{position:absolute;left:0;top:1681px;width:1200px;height:601px;background:linear-gradient(90deg,#111714 0%,#262a26 50%,#2f322f 80%,#3a3a38 100%)}
.reports h2{position:absolute;left:60px;top:108px;width:680px;color:#fff;font-size:32px;font-weight:700;line-height:30px}
.reports p{position:absolute;left:60px;top:205px;width:660px;color:#fff;font-size:19.5px;font-weight:600;line-height:30px}
.btn-lime{left:60px;top:306px;background:var(--lime)}
.reports-photo{position:absolute;left:812px;top:54px;width:328px;height:494px;background:linear-gradient(180deg,#5d6c52 0%,#7c8a82 40%,#9a9c92 75%,#5a544c 100%)}
.footer{position:absolute;left:0;top:2282px;width:1200px;height:99px;background:var(--night);color:#fff;font-size:13.5px;font-weight:700}
.copyright{position:absolute;left:38px;top:40px}
.contact{position:absolute;right:40px;top:36px;display:flex;align-items:center;gap:12px}
.social{display:flex;align-items:center;gap:5px;font-weight:600}
.social i{display:block;width:12px;height:12px}
</style>
</head>
<body>
<header class="hero" role="img" aria-label="Group of friends jumping joyfully in front of trees under a cloudy sky">
  <svg class="menu" viewBox="0 0 34 16"><rect y="0" width="34" height="2" fill="#fff"/><rect y="7" width="34" height="2" fill="#fff"/><rect y="14" width="34" height="2" fill="#fff"/></svg>
  <h1 class="hero-title">Harbor Crest Vitality</h1>
  <svg class="play" viewBox="0 0 60 60"><circle cx="30" cy="30" r="30" fill="var(--lime)"/><path d="M23 18 L43 30 L23 42 Z" fill="#1f2b20"/></svg>
</header>

<section class="assess">
  <h2>Assess your current Harbor Crest Vitality.</h2>
  <p>Complete our free life balance assessment to identify key areas where you will most benefit.</p>
  <a class="btn btn-teal">Learn More</a>
  <div class="assess-photo" role="img" aria-label="Woman stretching one arm upward in a green field"></div>
</section>
<svg class="wedge" width="588" height="36" viewBox="0 0 588 36"><polygon points="0,0 588,0 588,36" fill="var(--teal)"/></svg>

<section class="portal">
  <h2>Create a Harbor Crest Vitality Learning Portal account.</h2>
  <p>Get a <span class="trial">14 day free trial</span> to a wealth of learning activities, motivational videos and professional presentations on our learning portal designed specifically to address the eight essential areas of Harbor Crest Vitality.</p>
  <a class="btn btn-sky">Register Now</a>
</section>

<section class="reports" role="img" aria-label="Dim background of a woman with closed eyes">
  <h2>Get weekly reports on your progress and goal achievement.</h2>
  <p>Celebrate your success each week as you review your progress on each life balance area.</p>
  <a class="btn btn-lime">Learn More</a>
  <div class="reports-photo" role="img" aria-label="Woman meditating cross-legged on a wooden dock by a lake"></div>
</section>

<footer class="footer">
  <div class="copyright">Copyright © 2020 HarborCrestVitality</div>
  <div class="contact">
    <span>Contact With Us:</span>
    <span class="social"><i style="background:#e2366b"></i>Snapgram</span>
    <span class="social"><i style="background:var(--navy)"></i>Friendbook</span>
    <span class="social"><i style="background:var(--sky)"></i>Chirper</span>
  </div>
</footer>
</body>
</html>
```